Website Banner SKINS needed

We need some banner SKINS made for the front page of our website.
These skins must be in .psd format. We will use them for advertising new products and specials. We literally just want some cool, modern SKINS, no text needed (literally just cool backgrounds really)
1)The skins that we need are 845pix wide X 310pix tall.
2) The other skin we need is 845pix wide X 615pix tall. (this one will actually be SLIT by us into 3 equal pieces, so we want somehting that will look pleasing to the eye when cut)
We would like 5-7 skins for each size requested, that way we can change them as we need.
Please use this link for ideas on the colors, and types of SKINS we are looking for.
http://draft52.kelvorin.com/v/vspfiles/proofs/SwapYourKit/
I have attached our logo if needed. If these logos are in the skins, that would be okay but not necessarily required.

```html
<!DOCTYPE html>
<html lang="en">
<head>
<meta charset="utf-8">
<title>Banner Skins Preview</title>
<link rel="stylesheet" href="https://fonts.googleapis.com/css2?family=Ubuntu:wght@700&display=swap">
<style>
  :root {
    --backdrop: #2e2e2e;
    --backdrop-light: #3a3a3a;
    --heading: #d9d9d9;
    --heading-shadow: rgba(0, 0, 0, 0.85);
    --skin-core: #c20606;
    --skin-mid: #b00303;
    --skin-edge: #7e0000;
  }
  * { box-sizing: border-box; margin: 0; padding: 0; }
  html, body {
    width: 1200px;
    height: 911px;
    overflow: hidden;
    background: var(--backdrop);
  }
  .preview {
    position: relative;
    width: 1200px;
    height: 911px;
    overflow: hidden;
  }
  .preview__backdrop {
    position: absolute;
    inset: 0;
    background: radial-gradient(ellipse at center, var(--backdrop-light) 0%, var(--backdrop) 75%);
  }
  .preview__note {
    position: absolute;
    top: 14px;
    left: 0;
    width: 100%;
    text-align: center;
    font-family: "Ubuntu", sans-serif;
    font-weight: 700;
    font-size: 31px;
    line-height: 40px;
    color: var(--heading);
    text-shadow: 0 2px 4px var(--heading-shadow), 0 0 8px var(--heading-shadow);
  }
  .skin {
    position: absolute;
    left: 111px;
    width: 979px;
    height: 236px;
    background:
      radial-gradient(ellipse 75% 90% at 50% 55%, var(--skin-core) 0%, var(--skin-mid) 55%, var(--skin-edge) 100%);
    box-shadow:
      0 4px 14px rgba(0, 0, 0, 0.75),
      inset 0 0 40px rgba(60, 0, 0, 0.55),
      inset 0 -2px 0 rgba(0, 0, 0, 0.35);
  }
  .skin--top { top: 121px; }
  .skin--middle { top: 381px; }
  .skin--bottom { top: 642px; }
</style>
</head>
<body>
  <main class="preview">
    <div class="preview__backdrop" role="img" aria-label="Dark grey textured backdrop with a faint repeating brand pattern"></div>
    <p class="preview__note">Preview shows 845x615 cut into 3, but I’ve made 845x310 as well.<br>Background color easily changeable in background layer style.</p>
    <div class="skin skin--top"></div>
    <div class="skin skin--middle"></div>
    <div class="skin skin--bottom"></div>
  </main>
</body>
</html>
```